Gilt Corner Studio Shop Sign

Name of company
Gilt Corner Studio
Gilt Corner Studio is a picture framing shop and art gallery selling custom frames, art work and gifts.
Needing a design for shop front sign.

The Sign
The sign is above the shop front window and is approximately 12 feet wide by 43 inches high. White on black. White striped boarder that looks like a picture frame with Gilt Corner Studio in classic lettering including space for a phone number and it may or may not need to include description of services. Something cute in one area like a picture frame with a heart inside. A friendly feel like something that would be special and feels like yours. I have attached a photo of the existing sign to be replaced.

Thank you for your time.

```html
<!DOCTYPE html>
<html lang="en">
<head>
<meta charset="utf-8">
<title>Gilt Corner Studio – Shop Sign</title>
<link href="https://fonts.googleapis.com/css2?family=Bodoni+Moda:wght@400;500&family=Josefin+Sans:wght@300;400&display=swap" rel="stylesheet">
<style>
  :root {
    --paper: #ffffff;
    --sign-black: #000000;
    --sign-white: #ffffff;
    --ornament-tone: #8a8a8a;
  }
  * { margin: 0; padding: 0; box-sizing: border-box; }
  html, body {
    width: 1200px;
    height: 1200px;
    overflow: hidden;
    background: var(--paper);
  }
  .canvas {
    position: relative;
    width: 1200px;
    height: 1200px;
  }
  .shop-sign {
    position: absolute;
    left: 110px;
    top: 437px;
    width: 978px;
    height: 326px;
    background: var(--sign-black);
    color: var(--sign-white);
  }
  .sign-frame {
    position: absolute;
    inset: 0;
  }
  .corner-ornament {
    position: absolute;
    width: 58px;
    height: 58px;
    background: var(--ornament-tone);
  }
  .corner-ornament.top-left { left: 12px; top: 12px; }
  .corner-ornament.top-right { right: 12px; top: 12px; }
  .corner-ornament.bottom-left { left: 12px; bottom: 12px; }
  .corner-ornament.bottom-right { right: 12px; bottom: 12px; }
  .sign-content {
    position: absolute;
    inset: 0;
    display: flex;
    flex-direction: column;
    align-items: center;
  }
  .services-line {
    margin-top: 62px;
    display: flex;
    align-items: center;
    gap: 22px;
    font-family: "Josefin Sans", sans-serif;
    font-weight: 300;
    font-size: 26px;
    letter-spacing: 0.5px;
    line-height: 1;
  }
  .diamond {
    width: 8px;
    height: 8px;
    background: var(--sign-white);
    transform: rotate(45deg);
  }
  .business-name {
    margin-top: 22px;
    font-family: "Bodoni Moda", serif;
    font-weight: 400;
    font-size: 76px;
    line-height: 1;
    letter-spacing: 0.5px;
    white-space: nowrap;
  }
  .phone-line {
    margin-top: 26px;
    width: 808px;
    display: flex;
    align-items: center;
    gap: 22px;
    font-family: "Josefin Sans", sans-serif;
    font-weight: 300;
    font-size: 30px;
    line-height: 1;
    letter-spacing: 1px;
  }
  .rule {
    flex: 1;
    height: 1.5px;
    background: var(--sign-white);
  }
</style>
</head>
<body>
<div class="canvas">
  <section class="shop-sign" aria-label="Gilt Corner Studio shop sign">
    <svg class="sign-frame" width="978" height="326" viewBox="0 0 978 326" aria-hidden="true">
      <g fill="none" stroke="#ffffff" stroke-width="2">
        <rect x="12" y="12" width="954" height="302"/>
        <rect x="22" y="22" width="934" height="282"/>
        <rect x="36" y="36" width="906" height="254"/>
      </g>
    </svg>
    <div class="corner-ornament top-left" role="img" aria-label="Decorative scroll ornament at frame corner"></div>
    <div class="corner-ornament top-right" role="img" aria-label="Decorative scroll ornament at frame corner"></div>
    <div class="corner-ornament bottom-left" role="img" aria-label="Decorative scroll ornament at frame corner"></div>
    <div class="corner-ornament bottom-right" role="img" aria-label="Decorative scroll ornament at frame corner"></div>
    <div class="sign-content">
      <p class="services-line"><span class="diamond"></span>ART GALLERY AND CUSTOM FRAMES<span class="diamond"></span></p>
      <h1 class="business-name">GILT CORNER STUDIO</h1>
      <p class="phone-line"><span class="rule"></span>T. 01632 960418<span class="rule"></span></p>
    </div>
  </section>
</div>
</body>
</html>
```